New Electrical Contractor looking for local work

I have just started working for myself as an Electrical Contractor, based in the eastern suburbs of Melbourne. I want to advertise in the local area so hopefully I can create a client base that is close to home, so I thought a flyer that I could drop in letterboxes could be a good start. Most of my experience has been domestic houses, so ideally this is the work I would like to get more of.

Here is a list of the work I usually do:
Extensions / Renovations
Safety Switch and Switchboard Upgrades
LED Lighting including downlights/light fittings and LED strip light
Re-wires
Maintenance

I have also added a couple of images of LED strip lights and how they can be used in homes. There are a lot more on google images if anyone thinks they could be of use.

These are my details:
Business name - Dale Hurst Electrical
Phone - 0437 216 580
ABN - 42 318 570 264
REC - 38517
Email - hurstelectrical@sparkmailbox.net

I will attach my business logo and business card
Updates

Could I please ask for all designs to delete the "(contractors registration number)" text.

Only REC 38517 needs to be displayed.

Thank you kindly

Industry/Entity Type

Business

Requirements
Must have
• My contact details, ie. Name, Phone, email, ABN, REC etc

```html
<!DOCTYPE html>
<html lang="en">
<head>
<meta charset="utf-8">
<title>Dale Hurst Electrical – A5 Flyer</title>
<link rel="stylesheet" href="https://fonts.googleapis.com/css2?family=Arimo:wght@400;700&family=Tinos&display=swap">
<style>
  :root {
    --page: #ffffff;
    --ink: #111111;
    --muted: #333333;
    --frame: #000000;
    --card-edge: #d6d6d6;
    --accent: #1ba7d8;
    --denim-light: #9dbcd8;
    --denim-dark: #6a8db3;
    --grey-light: #c4c4c4;
    --grey-dark: #7c7c7c;
  }
  * { box-sizing: border-box; margin: 0; padding: 0; }
  html, body { width: 1200px; height: 900px; overflow: hidden; background: var(--page); }
  body { position: relative; font-family: "Arimo", Arial, sans-serif; color: var(--ink); }

  .flyer {
    position: absolute; top: 153px; width: 419px; height: 594px;
    background: var(--page); border: 1px solid var(--card-edge);
    box-shadow: 4px 4px 5px rgba(0,0,0,0.22);
  }
  .flyer--colour { left: 152px; }
  .flyer--mono { left: 628px; }

  .flyer__frame {
    position: absolute; left: 13px; top: 13px; width: 392px; height: 567px;
    border: 3px solid var(--frame);
  }

  .brand-mark {
    position: absolute; left: 40px; top: 30px; width: 80px; height: 96px;
    display: flex; flex-direction: column; align-items: center; justify-content: center; gap: 6px;
  }
  .brand-mark__dot { width: 26px; height: 26px; border-radius: 50%; background: var(--ink); }
  .brand-mark__name { font-size: 11px; font-weight: 700; color: var(--ink); }

  .contact { position: absolute; left: 141px; top: 46px; }
  .contact__name { font-size: 16.5px; font-weight: 700; letter-spacing: 0.1px; line-height: 19px; margin-bottom: 2px; }
  .contact__line { font-size: 11px; color: var(--muted); line-height: 15px; display: flex; align-items: center; gap: 5px; white-space: nowrap; }
  .contact__line svg { width: 11px; height: 9px; flex: none; }
  .contact__line--ids span + span { margin-left: 10px; }

  .hero {
    position: absolute; left: 21px; top: 144px; width: 383px; height: 199px;
  }
  .flyer--colour .hero { background: linear-gradient(180deg, var(--denim-light), var(--denim-dark)); }
  .flyer--mono .hero { background: linear-gradient(180deg, var(--grey-light), var(--grey-dark)); }

  .services { position: absolute; left: 55px; top: 366px; }
  .services__title { font-size: 23px; font-weight: 400; line-height: 28px; margin-bottom: 9px; white-space: nowrap; }
  .flyer--colour .services__title { color: var(--accent); }
  .flyer--mono .services__title { color: var(--ink); }
  .services__list { list-style: none; }
  .services__item {
    position: relative; padding-left: 18px; font-size: 14.4px; font-weight: 700;
    line-height: 17px; margin-bottom: 6px; white-space: nowrap;
  }
  .services__item::before {
    content: ""; position: absolute; left: 2px; top: 5px; width: 7px; height: 7px;
  }
  .flyer--colour .services__item::before { background: var(--accent); }
  .flyer--mono .services__item::before { background: var(--ink); }

  .caption {
    position: absolute; top: 760px; width: 419px; text-align: center;
    font-family: "Tinos", "Times New Roman", serif; font-size: 13px; color: var(--ink);
  }
  .caption--colour { left: 152px; }
  .caption--mono { left: 628px; }
</style>
</head>
<body>

<svg width="0" height="0" style="position:absolute">
  <symbol id="icon-phone" viewBox="0 0 12 10">
    <path d="M1 3 Q6 0 11 3 L10 4.5 L8 3.8 L8 3 Q6 2.4 4 3 L4 3.8 L2 4.5 Z M3 5 H9 L10 9 H2 Z" fill="currentColor"/>
  </symbol>
  <symbol id="icon-mail" viewBox="0 0 12 9">
    <rect x="0.5" y="0.5" width="11" height="8" fill="none" stroke="currentColor"/>
    <path d="M0.5 0.5 L6 5 L11.5 0.5" fill="none" stroke="currentColor"/>
  </symbol>
</svg>

<article class="flyer flyer--colour">
  <div class="flyer__frame"></div>
  <div class="brand-mark"><span class="brand-mark__dot"></span><span class="brand-mark__name">Dale Hurst</span></div>
  <div class="contact">
    <h1 class="contact__name">Dale Hurst Electrical</h1>
    <p class="contact__line"><svg><use href="#icon-phone"/></svg>0437 216 580</p>
    <p class="contact__line"><svg><use href="#icon-mail"/></svg>hurstelectrical@sparkmailbox.net</p>
    <p class="contact__line contact__line--ids"><span>REC 38517</span><span>ABN 42 318 570 264</span></p>
  </div>
  <div class="hero" role="img" aria-label="Photo of an electrician in a denim shirt and work gloves joining two power leads"></div>
  <section class="services">
    <h2 class="services__title">We provide services:</h2>
    <ul class="services__list">
      <li class="services__item">Extensions/Renovations</li>
      <li class="services__item">Safety Switch and Switchboard Upgrades</li>
      <li class="services__item">LED Lighting including downlights/<br>light fittings and LED strip light</li>
      <li class="services__item">Re-wires</li>
      <li class="services__item">Maintenance (mainly commercial)</li>
    </ul>
  </section>
</article>

<article class="flyer flyer--mono">
  <div class="flyer__frame"></div>
  <div class="brand-mark"><span class="brand-mark__dot"></span><span class="brand-mark__name">Dale Hurst</span></div>
  <div class="contact">
    <h1 class="contact__name">Dale Hurst Electrical</h1>
    <p class="contact__line"><svg><use href="#icon-phone"/></svg>0437 216 580</p>
    <p class="contact__line"><svg><use href="#icon-mail"/></svg>hurstelectrical@sparkmailbox.net</p>
    <p class="contact__line contact__line--ids"><span>REC 38517</span><span>ABN 42 318 570 264</span></p>
  </div>
  <div class="hero" role="img" aria-label="Black and white photo of an electrician in work gloves joining two power leads"></div>
  <section class="services">
    <h2 class="services__title">We provide services:</h2>
    <ul class="services__list">
      <li class="services__item">Extensions/Renovations</li>
      <li class="services__item">Safety Switch and Switchboard Upgrades</li>
      <li class="services__item">LED Lighting including downlights/<br>light fittings and LED strip light</li>
      <li class="services__item">Re-wires</li>
      <li class="services__item">Maintenance (mainly commercial)</li>
    </ul>
  </section>
</article>

<p class="caption caption--colour">A5 Size Flyer Design: Colored version</p>
<p class="caption caption--mono">A5 Size Flyer Design: Black &amp; White version</p>

</body>
</html>
```